Prairie Bend Comets

We are a travel softball organization based in Central IL. Girls are 8-14 yrs old. Looking for a modern website that is easily updated. Our current website is at www.prairiebendcomets-example.com. I want a tab for each team, 10U, 12U, 14U. I need a tab for pics. A tab for sponsors. A tap for files we have uploaded. And a about tab.

```html
<!DOCTYPE html>
<html lang="en">
<head>
<meta charset="utf-8">
<title>Prairie Bend Comets – Girls Travel Softball</title>
<link rel="stylesheet" href="https://fonts.googleapis.com/css2?family=Roboto+Condensed:wght@300;400;700&family=Open+Sans:wght@300;400;600&display=swap">
<style>
:root{
  --red:#e81c24;
  --ink:#222;
  --paper:#efefef;
  --white:#fff;
  --hero-top:#3a3a3a;
  --hero-bottom:#1c1c1c;
  --footer:#2a2a2a;
  --footer-field:#1c1c1c;
  --footer-text:#bdbdbd;
  --head:"Roboto Condensed",sans-serif;
  --body:"Open Sans",sans-serif;
}
*{box-sizing:border-box;margin:0;padding:0}
html,body{width:1200px;height:2500px;overflow:hidden}
body{position:relative;font-family:var(--body);color:var(--ink);background:var(--white)}
a{text-decoration:none}

/* Header / hero */
.hero{position:absolute;left:0;top:0;width:1200px;height:707px;overflow:hidden}
.hero-photo{position:absolute;inset:0;background:linear-gradient(180deg,var(--hero-top) 0%,var(--hero-bottom) 100%)}
.top-rule{position:absolute;left:0;top:0;width:1200px;height:4px;background:var(--red)}
.brand-tab{position:absolute;left:147px;top:0;width:261px;height:97px;background:var(--red);
  border-radius:0 0 18px 18px;display:flex;align-items:center;justify-content:center;gap:10px}
.brand-dot{width:16px;height:16px;border-radius:50%;background:var(--white)}
.brand-name{font-family:var(--head);font-weight:700;font-size:25px;color:var(--white);letter-spacing:.5px}
.nav a{position:absolute;top:38px;font-family:var(--head);font-size:15px;color:var(--white);text-transform:uppercase}
.nav a.active{color:var(--red)}
.hero-kicker{position:absolute;left:0;width:1200px;top:272px;text-align:center;font-family:var(--head);font-weight:300;font-size:40px;color:var(--white)}
.hero-title{position:absolute;left:0;width:1200px;top:322px;text-align:center;font-family:var(--head);font-weight:700;font-size:106px;line-height:1;color:var(--red);letter-spacing:1px}
.hero-rule{position:absolute;left:498px;top:453px;width:204px;height:1px;background:rgba(255,255,255,.45)}
.hero-text{position:absolute;left:320px;width:560px;top:490px;text-align:center;font-family:var(--head);font-size:14.5px;line-height:27px;color:#ddd}

/* Sections */
.section-title{position:absolute;left:0;width:1200px;text-align:center;font-family:var(--head);font-weight:300;font-size:32px;text-transform:uppercase}
.section-rule{position:absolute;left:568px;width:64px;height:3px}
.intro{position:absolute;left:0;top:707px;width:1200px;height:593px;background:var(--paper)}
.intro .section-title{top:120px;color:var(--red)}
.intro .section-rule{top:163px;background:#999}
.intro-text{position:absolute;left:133px;width:934px;top:200px;text-align:center;font-size:14px;line-height:27px;font-weight:300;color:#666}
.btn{position:absolute;background:var(--red);color:var(--white);font-family:var(--head);text-transform:uppercase;font-size:14.5px;display:flex;align-items:center;justify-content:center}
.intro .btn{left:517px;top:395px;width:176px;height:33px}

.gallery{position:absolute;left:0;top:1300px;width:1200px;height:558px;background:var(--red)}
.gallery-map{position:absolute;left:40px;top:10px;width:1120px;height:530px;
  background:radial-gradient(ellipse 48% 46% at 50% 45%,rgba(255,255,255,.06) 0%,transparent 100%)}
.gallery .section-title{top:82px;color:var(--white)}
.gallery .section-rule{top:125px;background:var(--white)}
.gallery-text{position:absolute;left:200px;width:800px;top:145px;text-align:center;font-size:13px;line-height:27px;color:var(--white)}
.thumb{position:absolute;top:250px;width:195px;height:193px;border:4px solid var(--white)}
.arrow{position:absolute;top:328px;width:22px;height:38px}

.sponsors{position:absolute;left:0;top:1858px;width:1200px;height:370px;background:var(--white)}
.sponsors .section-title{top:68px;color:var(--red)}
.sponsors .section-rule{top:113px;background:#aaa}
.sponsor{position:absolute;top:190px;height:80px;display:flex;align-items:center;justify-content:center;gap:8px;
  font-family:var(--head);font-weight:700;font-size:20px;color:#3a3a3a;white-space:nowrap}
.sponsor .mark{width:16px;height:16px;background:#3a3a3a;flex:none}
.sponsor .mark.round{border-radius:50%}

.footer{position:absolute;left:0;top:2228px;width:1200px;height:272px;background:var(--footer);color:var(--footer-text)}
.footer-brand{position:absolute;left:103px;top:40px;width:175px;height:80px;display:flex;align-items:center;gap:9px;
  font-family:var(--head);font-weight:700;font-size:24px;color:#cfcfcf;line-height:1.05}
.footer-brand .brand-dot{background:#cfcfcf;flex:none}
.social{position:absolute;left:120px;top:152px;width:137px;height:45px;border:1px solid #999;border-radius:3px;
  display:flex;align-items:center;gap:9px;padding-left:12px;font-family:var(--head);font-size:14px;color:#ddd}
.social .mark{width:16px;height:16px;background:#ddd}
.footer h4{position:absolute;top:35px;font-family:var(--head);font-weight:400;font-size:16px;color:var(--white);text-transform:uppercase}
.links a{position:absolute;font-size:12px;color:#ddd;padding-left:16px}
.links a::before{content:"";position:absolute;left:0;top:5px;border-left:5px solid var(--red);border-top:4px solid transparent;border-bottom:4px solid transparent}
.news-text{position:absolute;left:763px;top:65px;width:300px;font-size:12px;line-height:22px}
.field{position:absolute;left:763px;top:125px;width:299px;height:37px;background:var(--footer-field);font-size:12.5px;color:#aaa;padding:10px 0 0 16px}
.footer .btn{left:767px;top:180px;width:118px;height:29px;font-family:var(--body);font-weight:600;font-size:13px;text-transform:none}
.footer-rule{position:absolute;left:97px;top:227px;width:1006px;height:1px;background:#444}
.copyright{position:absolute;left:0;width:1200px;top:241px;text-align:center;font-size:11.5px;color:#999}
</style>
</head>
<body>

<header class="hero">
  <div class="hero-photo" role="img" aria-label="Dimmed background photo of a softball and bat"></div>
  <div class="top-rule"></div>
  <div class="brand-tab"><span class="brand-dot"></span><span class="brand-name">Prairie Bend Comets</span></div>
  <nav class="nav">
    <a class="active" href="#" style="left:520px">Home</a>
    <a href="#" style="left:587px">Teams</a>
    <a href="#" style="left:655px">Gallery</a>
    <a href="#" style="left:752px">Files</a>
    <a href="#" style="left:822px">About</a>
    <a href="#" style="left:903px">Sponsors</a>
    <a href="#" style="left:1007px">Contacts</a>
  </nav>
  <p class="hero-kicker">NEWLY FORMED GIRLS TRAVEL/COMPETITIVE</p>
  <h1 class="hero-title">SOFTBALL TEAM</h1>
  <div class="hero-rule"></div>
  <p class="hero-text">Prairie Bend Comets is a girls travel softball organisation, based out of Prairie Bend, IL but with players from all over Central Illinois</p>
</header>

<section class="intro">
  <h2 class="section-title">Introduction</h2>
  <div class="section-rule"></div>
  <p class="intro-text">It is a long established fact that a reader will be distracted by the readable content of a page when looking at its layout. The point of using Lorem Ipsum is that it has a more-or-less normal distribution of letters, as opposed to using 'Content here, content here', making it look like readable English. Many desktop publishing packages and web page editors now use Lorem Ipsum as their default model text, and a search for 'lorem ipsum' will uncover many web sites still in their infancy. Various versions have evolved over the years, sometimes by accident, sometimes on purpose (injected humour and the like).</p>
  <a class="btn" href="#">Click for more details</a>
</section>

<section class="gallery">
  <div class="gallery-map" role="img" aria-label="Faint world map pattern"></div>
  <h2 class="section-title">Picture Gallery</h2>
  <div class="section-rule"></div>
  <p class="gallery-text">Lorem Ipsum is simply dummy text of the printing and typesetting industry. Lorem Ipsum has been the industry's standard dummy text ever since the 1500s, when an unknown printer took a galley of type and scrambled it to make a type specimen book.</p>
  <div class="thumb" style="left:160px;background:linear-gradient(180deg,#9bb07e,#6e8c52)" role="img" aria-label="Photo of a player at bat in a red helmet"></div>
  <div class="thumb" style="left:392px;background:linear-gradient(180deg,#8fa56f,#b55050)" role="img" aria-label="Team photo of players in red and white uniforms"></div>
  <div class="thumb" style="left:623px;background:linear-gradient(180deg,#8fa37a,#b9aa8c)" role="img" aria-label="Photo of a player leading off a base"></div>
  <div class="thumb" style="left:855px;background:linear-gradient(180deg,#8fb7e3,#a57e5c)" role="img" aria-label="Photo of a player holding a softball on the field"></div>
  <svg class="arrow" style="left:56px" viewBox="0 0 22 38"><polyline points="18,3 4,19 18,35" fill="none" stroke="#fff" stroke-width="2"/></svg>
  <svg class="arrow" style="left:1130px" viewBox="0 0 22 38"><polyline points="4,3 18,19 4,35" fill="none" stroke="#fff" stroke-width="2"/></svg>
</section>

<section class="sponsors">
  <h2 class="section-title">Our Sponsors</h2>
  <div class="section-rule"></div>
  <div class="sponsor" style="left:110px;width:175px"><span class="mark"></span>KRVX Radio</div>
  <div class="sponsor" style="left:300px;width:160px"><span class="mark"></span>Harbor Mutual</div>
  <div class="sponsor" style="left:478px;width:210px"><span class="mark round"></span>Meadowland Bank</div>
  <div class="sponsor" style="left:705px;width:170px">Civic Service Club</div>
  <div class="sponsor" style="left:880px;width:215px">Halvorsen Bros. Trucking</div>
</section>

<footer class="footer">
  <div class="footer-brand"><span class="brand-dot"></span><span>Prairie Bend Comets</span></div>
  <div class="social"><span class="mark"></span>Find us online</div>

  <h4 style="left:420px">Quick Links</h4>
  <div class="links">
    <a href="#" style="left:424px;top:76px">Home</a>
    <a href="#" style="left:424px;top:109px">Gallery</a>
    <a href="#" style="left:424px;top:141px">Files</a>
    <a href="#" style="left:424px;top:174px">About</a>
    <a href="#" style="left:529px;top:76px">Teams</a>
    <a href="#" style="left:529px;top:109px">Sponsors</a>
    <a href="#" style="left:529px;top:141px">Schedule/ Result</a>
    <a href="#" style="left:529px;top:174px">Contacts</a>
  </div>

  <h4 style="left:763px">Newsletter Signup</h4>
  <p class="news-text">Fill in the Details Below to Subscribe for Regular Newsletters and events</p>
  <div class="field">Your Email Address</div>
  <a class="btn" href="#">Subscribe Now</a>

  <div class="footer-rule"></div>
  <p class="copyright">© Copyright 2017 | All Rights Reserved</p>
</footer>

</body>
</html>
```